Tea Brand needs a packaging design

We need a Tea packaging design for a new tea brand based in Kenya called 'Vela Tea'. Kenya is home to the finest teas in the world and Vela tea looks to embody that fact. Vela Tea uses the most premium of Kenyan Tea, Black tea, Purple tea, White Tea, Green tea, Hibiscus Tea and Moringa Tea. Vela Tea is handpicked from Kenya's highlands. This project will include the look and feel of the different teas described above. The copy on the main face of the box should read 'Premium Kenyan Tea' The box will contain 25 tagged tea bags, with a net weight of 50 gms. On one side of the box will read 'packaging instructions' To fully savour this Vela premium tea, use one tea bag for each cup, add some freshly bolded water and wait for 2 minutes as you enjoy the sweet aroma of our tea, stir and serve' Ingredients : Black Tea, and for the others the same : Hibiscus Tea, Green Tea, Purple Tea, White tea. should also feature on the label: Produce of Kenya.

Target Market(s)

Premium Market, Global Brand so must have a premium look and feel

Industry/Entity Type

Retail

Font styles to use
Script

Requirements
Must have
• Some natural , earthy feel, a touch of Africa.
Nice to have
• I'd like the package to have a simple and clean look
Should not have
• Should not have a cup of tea. green and yellow should not be the dominant colours

```html
<!DOCTYPE html>
<html lang="en">
<head>
<meta charset="utf-8">
<title>Vela Teas – Packaging Range</title>
<link rel="stylesheet" href="https://fonts.googleapis.com/css2?family=Cinzel:wght@400;700&family=Josefin+Sans:wght@400&display=swap">
<style>
  :root {
    --backdrop: #a9a9a9;
    --box-body: #262626;
    --box-body-light: #323232;
    --lid-black: #0b0b0b;
    --lid-purple: #62247f;
    --lid-green: #778a28;
    --wordmark-light: #ffffff;
    --wordmark-earth: #8a6a60;
    --tea-lime: #a9bb45;
    --art-light: #c9d978;
    --art-mid: #9fb544;
    --grass: #0d0d0d;
  }
  * { margin: 0; padding: 0; box-sizing: border-box; }
  html, body { width: 1200px; height: 600px; overflow: hidden; }
  body {
    background: linear-gradient(180deg, #8e8e8e 0%, var(--backdrop) 55%, #cfcfcf 100%);
    font-family: "Cinzel", serif;
    display: flex;
    justify-content: center;
    align-items: center;
    gap: 30px;
  }
  .tea-box { width: 340px; display: flex; flex-direction: column; }
  .box-top {
    height: 120px;
    display: flex;
    align-items: center;
    justify-content: center;
  }
  .tea-box--black .box-top { background: var(--lid-black); }
  .tea-box--purple .box-top { background: var(--lid-purple); }
  .tea-box--green .box-top { background: var(--lid-green); }
  .box-front {
    height: 400px;
    background: linear-gradient(135deg, var(--box-body-light) 0%, var(--box-body) 45%, #1c1c1c 100%);
    display: flex;
    flex-direction: column;
    align-items: center;
  }
  .lid-front {
    height: 100px;
    width: 100%;
    display: flex;
    align-items: center;
    justify-content: center;
  }
  .lid-band { height: 9px; width: 100%; }
  .tea-box--black .lid-band { background: var(--lid-black); }
  .tea-box--purple .lid-band { background: var(--lid-purple); }
  .tea-box--green .lid-band { background: var(--lid-green); }
  .wordmark {
    font-family: "Josefin Sans", sans-serif;
    font-weight: 400;
    letter-spacing: 3px;
    text-align: center;
    line-height: 1;
    display: flex;
    align-items: center;
    gap: 8px;
  }
  .wordmark-dot { width: 8px; height: 8px; border-radius: 50%; background: currentColor; }
  .wordmark--top { color: var(--wordmark-light); font-size: 28px; }
  .wordmark--front { color: var(--wordmark-earth); font-size: 30px; }
  .wildlife-art {
    margin-top: 28px;
    width: 250px;
    height: 170px;
    background:
      linear-gradient(180deg, transparent 72%, var(--grass) 100%),
      radial-gradient(ellipse at 50% 45%, var(--art-light) 0%, var(--art-mid) 55%, #3c4620 100%);
    border-radius: 40% 40% 6px 6px;
  }
  .tea-name {
    margin-top: 22px;
    color: var(--tea-lime);
    font-weight: 700;
    font-size: 22px;
    letter-spacing: 1px;
  }
  .tagline {
    margin-top: 8px;
    color: var(--tea-lime);
    font-size: 10.5px;
    letter-spacing: 0.8px;
  }
</style>
</head>
<body>
  <section class="tea-box tea-box--black">
    <div class="box-top"><div class="wordmark wordmark--top"><span class="wordmark-dot"></span>VELA TEAS</div></div>
    <div class="box-front">
      <div class="lid-front"><div class="wordmark wordmark--front"><span class="wordmark-dot"></span>VELA TEAS</div></div>
      <div class="lid-band"></div>
      <div class="wildlife-art" role="img" aria-label="Lime watercolour silhouette of an elephant walking through dark savanna grass"></div>
      <h2 class="tea-name">BLACK TEA</h2>
      <p class="tagline">- THE PREMIUM TASTE OF AFRICAN TEA -</p>
    </div>
  </section>

  <section class="tea-box tea-box--purple">
    <div class="box-top"><div class="wordmark wordmark--top"><span class="wordmark-dot"></span>VELA TEAS</div></div>
    <div class="box-front">
      <div class="lid-front"><div class="wordmark wordmark--front"><span class="wordmark-dot"></span>VELA TEAS</div></div>
      <div class="lid-band"></div>
      <div class="wildlife-art" role="img" aria-label="Lime watercolour silhouette of a rhinoceros standing in dark savanna grass"></div>
      <h2 class="tea-name">PURPLE TEA</h2>
      <p class="tagline">- THE PREMIUM TASTE OF AFRICAN TEA -</p>
    </div>
  </section>

  <section class="tea-box tea-box--green">
    <div class="box-top"><div class="wordmark wordmark--top"><span class="wordmark-dot"></span>VELA TEAS</div></div>
    <div class="box-front">
      <div class="lid-front"><div class="wordmark wordmark--front"><span class="wordmark-dot"></span>VELA TEAS</div></div>
      <div class="lid-band"></div>
      <div class="wildlife-art" role="img" aria-label="Lime watercolour silhouette of a lion prowling through dark savanna grass"></div>
      <h2 class="tea-name">GREEN TEA</h2>
      <p class="tagline">- THE PREMIUM TASTE OF AFRICAN TEA -</p>
    </div>
  </section>
</body>
</html>
```